Security business needs NDA formatted.

We need our NDA formatted properly and to look modern with our logo. Anybody can paste words into a document, but we need something clean, modern, DocuSign-friendly, and stylish.

```html
<!DOCTYPE html>
<html lang="en">
<head>
<meta charset="utf-8">
<title>Non-Disclosure Agreement – Terravista</title>
<link href="https://fonts.googleapis.com/css2?family=Carlito:wght@400;700&display=swap" rel="stylesheet">
<style>
:root{
  --canvas:#e6e6e6;
  --paper:#ffffff;
  --ink:#222222;
  --band:#000000;
  --band-text:#ffffff;
  --muted:#c9c9c9;
  --brand-grey:#8a8a8a;
  --edge:#d3d3d3;
}
*{margin:0;padding:0;box-sizing:border-box}
html,body{width:1200px;height:815px;overflow:hidden;background:var(--canvas)}
body{position:relative;font-family:"Carlito",Calibri,sans-serif;color:var(--ink)}
.page{position:absolute;width:283px;height:368px;background:var(--paper);border:1px solid var(--edge);overflow:hidden;font-size:4.4px;line-height:8.1px}
.row-top{top:27px}.row-bottom{top:404px}
.col-1{left:29px}.col-2{left:319px}.col-3{left:611px}.col-4{left:901px}

.page-footer{position:absolute;left:25px;right:25px;top:349px;height:12px;display:flex;align-items:center;justify-content:space-between}
.footer-brand{display:flex;align-items:center;gap:2px;font-size:5.6px;font-weight:700;color:var(--brand-grey)}
.footer-brand .dot{width:9px;height:9px;border-radius:50%;background:#9a9a9a}
.page-number{color:var(--muted);font-size:4.2px}

.title-band{background:var(--band);color:var(--band-text);font-weight:700}
.title-band.centered{height:33px;display:flex;align-items:flex-end;justify-content:center;padding-bottom:8px;letter-spacing:1.6px;font-size:4.6px}
.title-band.heading{height:36px;display:flex;align-items:flex-end;padding:0 0 5px 23px;font-size:4.4px}
.section-band{background:var(--band);color:var(--band-text);font-weight:700;height:14px;display:flex;align-items:center;padding-left:40px;font-size:4.4px;margin:6px 0 7px}

.body{padding:0 28px 0 27px}
.clause{display:flex;margin-bottom:6.5px}
.clause .num{width:14px;flex:none}
.clause .text{flex:1}
.sub{display:flex;margin-top:6px}
.sub .num{width:14px;flex:none}
.sub .text{flex:1}
.tight .sub{margin-top:0}
.justify{text-align:justify}

/* cover page */
.cover-image{position:absolute;left:0;top:0;width:283px;height:80px;background:linear-gradient(180deg,#1f3448 0%,#3c5670 45%,#6d7e8e 75%,#2a3440 100%)}
.cover-brand{position:absolute;left:66px;top:20px;display:flex;align-items:center;gap:6px;color:#fff}
.cover-brand .mark{width:37px;height:37px;border-radius:50%;background:#fff}
.cover-brand .name{font-size:19px;font-weight:700;line-height:20px}
.cover-brand .tag{font-size:7px;letter-spacing:1px;line-height:9px}
.cover-title{position:absolute;left:0;top:80px;width:283px;height:26px;background:var(--band);color:#fff;font-weight:700;font-size:6.6px;letter-spacing:1.8px;display:flex;align-items:center;justify-content:center}
.abs{position:absolute}
.center-line{left:0;width:283px;text-align:center}
.party-tab{position:absolute;left:0;width:60px;height:12px;background:var(--band);color:#fff;font-weight:700;font-size:4.4px;letter-spacing:1.4px;display:flex;align-items:center;justify-content:center}
.part-label{right:25px;text-align:right}
.background-band{position:absolute;left:0;top:255px;width:283px;height:12px;background:var(--band);color:#fff;font-weight:700;letter-spacing:1.6px;display:flex;align-items:center;justify-content:center;font-size:4.4px}
.background-body{position:absolute;left:25px;right:34px;top:271px}
.rule{display:inline-block;border-bottom:0.6px solid var(--ink);vertical-align:baseline}
.signature{position:absolute;left:149px;width:110px}
</style>
</head>
<body>

<!-- Page 1 -->
<section class="page row-top col-1">
  <div class="cover-image" role="img" aria-label="Night city skyline photo with network light trails"></div>
  <div class="cover-brand">
    <div class="mark"></div>
    <div><div class="name">Terravista</div><div class="tag">Geospatial Intelligence</div></div>
  </div>
  <div class="cover-title">NON-DISCLOSURE AGREEMENT</div>

  <div class="abs center-line" style="top:116px"><b>THIS NON-DISCLOSURE AGREEMENT</b> ("the Agreement")</div>
  <div class="abs center-line" style="top:129px">dated this <span class="rule" style="width:97px"></span>day of</div>
  <div class="abs center-line" style="top:142px">, <span class="rule" style="width:42px"></span>.</div>

  <div class="party-tab" style="top:151px">BETWEEN:</div>
  <div class="abs center-line" style="top:167px;line-height:8px">ACME of 58 Harbor Row, CA, 95410, USA (the<br>"Company")</div>
  <div class="abs part-label" style="top:196px">OF THE FIRST PART</div>

  <div class="party-tab" style="top:206px">- AND -</div>
  <div class="abs center-line" style="top:222px;line-height:8px">COMPANY NAME of COMPANY ADDRESS<br>(the "Evaluator")</div>
  <div class="abs part-label" style="top:244px">OF THE SECOND PART</div>

  <div class="background-band">BACKGROUND</div>
  <div class="background-body">
    <div class="clause"><div class="num">A.</div><div class="text">ACME has proprietary information and know-how relating to certain investigation tools and tactics (the "Company").</div></div>
    <div class="clause"><div class="num">B.</div><div class="text">In connection with the Evaluator evaluating the Invention for possible patent, development, and marketing (the "Permitted Purpose"), the Evaluator has requested certain confidential information (the "Confidential Information") regarding the Company.</div></div>
    <div><b>IN CONSIDERATION OF</b> and as a condition of the Company providing the Confidential Information to the Evaluator in addition to other valuable consideration, the receipt and sufficiency of which consideration is hereby acknowledged, the parties to this Agreement agree as follows:</div>
  </div>
  <footer class="page-footer"><div class="footer-brand"><span class="dot"></span>Terravista</div><div class="page-number">Page 1 of 8</div></footer>
</section>

<!-- Page 2 -->
<section class="page row-top col-2">
  <div class="title-band centered">CONFIDENTIAL INFORMATION</div>
  <div class="body" style="padding-top:6px">
    <div class="clause"><div class="num">1.</div><div class="text">All written and oral information and materials disclosed or provided by the Company to the Evaluator under this Agreement constitute Confidential Information regardless of whether such information was provided before or after the date of this Agreement or how it was provided to the Evaluator.</div></div>
    <div class="clause"><div class="num">2.</div><div class="text">'Confidential Information' means all data and information relating to the invention as well as data and information relating to the Company, including but not limited to, the following:
      <div class="sub"><div class="num">a.</div><div class="text">'Business Operations' which includes internal personnel and financial information of the Company, vendor names and other vendor information (including vendor characteristics, services and agreements), purchasing and internal cost information, internal services and operational manuals, external business contacts including those stored on social media accounts or other similar platforms or databases operated by the Company, and the manner and methods of conducting the Company's business;</div></div>
      <div class="sub"><div class="num">b.</div><div class="text">'Customer Information' which includes names of customers of the Company, their representatives, all customer contact information, contracts and their contents and parties, customer services, data provided by customers and the type, quantity and specifications of products and services purchased, leased, licensed or received by customers of the Company;</div></div>
      <div class="sub"><div class="num">c.</div><div class="text">'Intellectual Property' which includes information relating to the Company's proprietary rights prior to any public disclosure of such information, including but not limited to the nature of the proprietary rights, production data, technical and engineering data, technical concepts, test data and test results, simulation results, the status and details of research and development of products and services, and information regarding acquiring, protecting, enforcing and licensing proprietary rights (including patents, copyrights and trade secrets);</div></div>
      <div class="sub"><div class="num">d.</div><div class="text">'Service Information' which includes all data and information relating to the services provided by the Company, including but not limited to, plans, schedules, manpower, inspection, and training information;</div></div>
      <div class="sub"><div class="num">e.</div><div class="text">'Product Information' which includes all specifications for products of the Company as well as work product resulting from or related to work or projects of the Company, of any type or form in any stage of actual or anticipated research and development;</div></div>
      <div class="sub"><div class="num">f.</div><div class="text">'Production Processes' which includes processes used in the creation, production and manufacturing of the work product of the Company, including but not limited to, formulas, patterns, molds, models, methods, techniques, specifications, processes, procedures, equipment, devices, programs, and designs;</div></div>
    </div></div>
  </div>
  <footer class="page-footer"><div class="footer-brand"><span class="dot"></span>Terravista</div><div class="page-number">Page 2 of 8</div></footer>
</section>

<!-- Page 3 -->
<section class="page row-top col-3">
  <div class="body" style="padding-top:19px;padding-left:41px">
    <div class="sub" style="margin-top:0"><div class="num">g.</div><div class="text">'Accounting Information' which includes, without limitation, all financial statements, annual reports, balance sheets, company asset information, company liability information, revenue and expense reporting, profit and loss reporting, cash flow reporting, accounts receivable, accounts payable, Company reporting, purchasing information and payroll information of the Company;</div></div>
    <div class="sub"><div class="num">h.</div><div class="text">'Marketing and Development Information' which includes marketing and development plans of the Company, price and cost data, price and fee amounts, pricing and billing policies, quoting procedures, marketing techniques and methods of obtaining business, forecasts and forecast assumptions and volumes, and future plans and potential strategies of the Company which have been or are being discussed;</div></div>
    <div class="sub"><div class="num">i.</div><div class="text justify">'Computer Technology' which includes all scientific and technical information or material of the Company, pertaining to any machine, appliance or process, including but not limited to, specifications, proposals, models, designs, formulas, test results and reports, analyses, simulation results, tables of operating conditions, materials, components, industrial skills, operating and testing procedures, shop practices, know-how and show-how;</div></div>
    <div class="sub"><div class="num">j.</div><div class="text">'Proprietary Computer Code' which includes all sets of statements, instructions or programs of the Company, whether in human readable or machine readable form, that are expressed, fixed, embodied or stored in any manner and that can be used directly or indirectly in a computer ('Computer Programs'); any report format, design or drawing created or produced by such Computer Programs; and all documentation, design specifications and charts, and operating procedures which support the Computer Programs; and</div></div>
    <div class="sub"><div class="num">k.</div><div class="text">Confidential Information will also include any information that has been disclosed by a third party to the Company and is protected by a non-disclosure agreement entered into between the third party and the Company.</div></div>
  </div>
  <div class="body" style="padding-top:7px;padding-left:27px">
    <div class="clause"><div class="num">3.</div><div class="text">Confidential Information will not include the following information:
      <div class="tight">
      <div class="sub"><div class="num">a.</div><div class="text">Information that is generally known in the industry of the Company;</div></div>
      <div class="sub"><div class="num">b.</div><div class="text">Information that is now or subsequently becomes generally available to the public through no wrongful act of the Evaluator;</div></div>
      <div class="sub"><div class="num">c.</div><div class="text">Information rightly in the possession of the Evaluator prior to the disclosure to the Evaluator by the Company;</div></div>
      <div class="sub"><div class="num">d.</div><div class="text">Information that is independently created by the Evaluator without direct or indirect use of the Confidential Information; or</div></div>
      <div class="sub"><div class="num">e.</div><div class="text">Information that the Evaluator rightfully obtains from a third party who has the right to transfer or disclose it.</div></div>
      </div>
    </div></div>
  </div>
  <footer class="page-footer"><div class="footer-brand"><span class="dot"></span>Terravista</div><div class="page-number">Page 3 of 8</div></footer>
</section>

<!-- Page 4 -->
<section class="page row-top col-4">
  <div class="title-band heading">Obligations of Non-Disclosure</div>
  <div class="body" style="padding-top:10px;padding-left:26px">
    <div class="clause"><div class="num">4.</div><div class="text">Except as otherwise provided in this Agreement, the Evaluator must not disclose the Confidential Information.</div></div>
    <div class="clause"><div class="num">5.</div><div class="text">Except as otherwise provided in this Agreement, the Confidential Information will remain the exclusive property of the Company and will only be used by the Evaluator for the Permitted Purpose. The Evaluator will not use the Confidential Information for any purpose that might be directly or indirectly detrimental to the Company or any associated affiliates or subsidiaries.</div></div>
    <div class="clause"><div class="num">6.</div><div class="text">The obligations to ensure and prevent the disclosure of the Confidential Information imposed on the Evaluator in this Agreement and any obligations to provide notice under this Agreement will survive the expiration or termination, as the case may be, of this Agreement and those obligations will last indefinitely.</div></div>
    <div class="clause"><div class="num">7.</div><div class="text">The Evaluator may disclose any of the Confidential Information:
      <div class="sub"><div class="num">a.</div><div class="text">to such employees, agents, representatives and advisors of the Evaluator that have a need to know for the Permitted Purpose provided that:
        <div class="sub"><div class="num">i.</div><div class="text">the Evaluator has informed such personnel of the confidential nature of the Confidential Information;</div></div>
        <div class="sub"><div class="num">ii.</div><div class="text">such personnel agree to be legally bound to the same burdens of non-disclosure and non-use as the Evaluator;</div></div>
        <div class="sub"><div class="num">iii.</div><div class="text">the Evaluator agrees to take all necessary steps to ensure that the terms of this Agreement are not violated by such personnel; and</div></div>
        <div class="sub" style="margin-top:1px"><div class="num">iv.</div><div class="text">the Evaluator agrees to be responsible for and indemnify the Company for any breach of this Agreement by its personnel.</div></div>
      </div></div>
      <div class="sub"><div class="num">b.</div><div class="text">to a third party where the Company has consented in writing to such disclosure; and</div></div>
      <div class="sub"><div class="num">c.</div><div class="text">to the extent required by law or by the request or requirement of any judicial, legislative, administrative or other governmental body.</div></div>
    </div></div>
    <div class="clause"><div class="num">8.</div><div class="text">The Evaluator agrees to retain all Confidential Information at its usual place of business and to store all Confidential Information separate from other information and documents held in the same location. Further, the Confidential Information may not be used, reproduced, transformed, or stored on a computer or device that is accessible to persons to whom disclosure may not be made, as set out in this Agreement.</div></div>
  </div>
  <footer class="page-footer"><div class="footer-brand"><span class="dot"></span>Terravista</div><div class="page-number">Page 4 of 8</div></footer>
</section>

<!-- Page 5 -->
<section class="page row-bottom col-1">
  <div class="title-band heading" style="padding-left:40px">Non-Solicitation</div>
  <div class="body" style="padding-top:8px;padding-left:25px;padding-right:28px">
    <div class="clause"><div class="num">9.</div><div class="text">The Evaluator, its affiliates, subsidiaries and representatives will not, from the date of this Agreement for a period of two years, directly or indirectly solicit for employment or employ any person who is now employed or retained by the Company or any affiliate of the Company without the prior written consent of the Company.</div></div>
  </div>
  <div class="section-band">Non-Competition</div>
  <div class="body" style="padding-left:25px">
    <div class="clause"><div class="num">10.</div><div class="text">Other than with the express written consent of the Company, which consent may not be unreasonably withheld, the Evaluator will not, from the date of this Agreement for a period of two years, be directly or indirectly involved with a business which is in direct competition with the Company in the market for the Invention.</div></div>
  </div>
  <div class="section-band">Ownership and Title</div>
  <div class="body" style="padding-left:25px">
    <div class="clause"><div class="num">11.</div><div class="text">Nothing contained in this Agreement will grant to or create in the Evaluator, either expressly or impliedly, any right, title, interest or license in or to the intellectual property of the Company.</div></div>
  </div>
  <div class="section-band" style="margin-top:10px">Remedies</div>
  <div class="body" style="padding-left:25px">
    <div class="clause"><div class="num">12.</div><div class="text">The Evaluator agrees and acknowledges that the Confidential Information is of a proprietary and confidential nature and that any disclosure of the Confidential Information to a third party in breach of this Agreement cannot be reasonably or adequately compensated for in money damages and would cause irreparable injury to the Company. Accordingly, the Evaluator agrees that the Company is entitled to, in addition to all other rights and remedies available to it at law or in equity, an injunction restraining the Evaluator, any of its personnel, and any agents of the Evaluator, from directly or indirectly committing or engaging in any act restricted by this Agreement in relation to the Confidential Information.</div></div>
  </div>
  <div class="section-band">Return of Confidential Information</div>
  <div class="body" style="padding-left:25px">
    <div class="clause"><div class="num">13.</div><div class="text">The Company may at any time request the return of all Confidential Information from the Evaluator. Upon the request of the Company, or in the event that the Evaluator ceases to require use of the Confidential Information, or upon the expiration or termination of this Agreement, the Evaluator will:
      <div class="sub"><div class="num">a.</div><div class="text">return all Confidential Information to the Company;</div></div>
      <div class="sub"><div class="num">b.</div><div class="text">provide a certificate to the Company to the effect that the Evaluator has returned all</div></div>
    </div></div>
  </div>
  <footer class="page-footer"><div class="footer-brand"><span class="dot"></span>Terravista</div><div class="page-number">Page 5 of 8</div></footer>
</section>

<!-- Page 6 -->
<section class="page row-bottom col-2">
  <div class="body" style="padding-top:18px;padding-left:56px">Confidential Information to the Company.</div>
  <div class="section-band" style="margin-top:3px">Notices</div>
  <div class="body" style="padding-left:27px">
    <div class="clause"><div class="num">14.</div><div class="text">In the event that the Evaluator is required in a civil, criminal or regulatory proceeding to disclose any part of the Confidential Information, the Evaluator will give to the Company prompt written notice of such request so the Company may seek an appropriate remedy or alternatively to waive the Evaluator's compliance with the provisions of this Agreement in regards to the request.</div></div>
    <div class="clause"><div class="num">15.</div><div class="text">If the Evaluator loses or makes unauthorized disclosure of any of the Confidential Information, the Evaluator will immediately notify the Company and take all reasonable steps necessary to retrieve the lost or improperly disclosed Confidential Information.</div></div>
    <div class="clause"><div class="num">16.</div><div class="text">Any notices or delivery required in this Agreement will be deemed completed when hand- delivered, delivered by agent, or seven days after being placed in the post, postage prepaid, to the parties at the addresses contained in this Agreement or as the parties may later designate in writing.</div></div>
    <div class="clause"><div class="num">17.</div><div class="text">The addresses for any notice to be delivered to any of the parties to this Agreement are as follows:
      <div class="sub"><div class="num">a.</div><div class="text">Name: ACME<br>Address: 1190 Lakeview Ave, Holland, MI 49424, USA</div></div>
      <div class="sub" style="margin-top:0"><div class="num">b.</div><div class="text">Name: COMPANY NAME Address:<br>COMPANY ADDRESS</div></div>
    </div></div>
  </div>
  <div class="section-band" style="margin-top:19px">Representations</div>
  <div class="body" style="padding-left:27px">
    <div class="clause"><div class="num">18.</div><div class="text">In providing the Confidential Information, the Company makes no representations, either expressly or impliedly as to its adequacy, sufficiency, completeness, correctness or its lack of defect of any kind, including any patent or trademark infringement that may result from the use of such information.</div></div>
  </div>
  <div class="section-band">Further Agreements</div>
  <div class="body" style="padding-left:27px">
    <div class="clause"><div class="num">19.</div><div class="text">In the event that the Evaluator finds that the Invention is worthy of being patented, developed and marketed, the Company and the Evaluator may negotiate an additional agreement to define all their respective rights regarding such patenting, marketing, and development.</div></div>
  </div>
  <footer class="page-footer"><div class="footer-brand"><span class="dot"></span>Terravista</div><div class="page-number">Page 6 of 8</div></footer>
</section>

<!-- Page 7 -->
<section class="page row-bottom col-3">
  <div class="title-band heading" style="padding-left:41px">Termination</div>
  <div class="body" style="padding-top:4px;padding-left:26px">
    <div class="clause"><div class="num">20.</div><div class="text">Either party may terminate this Agreement by providing written notice to the other party. Except as otherwise provided in this Agreement, all rights and obligations under this Agreement will terminate at that time.</div></div>
  </div>
  <div class="section-band" style="margin-top:10px;padding-left:41px">Assignment</div>
  <div class="body" style="padding-left:26px">
    <div class="clause"><div class="num">21.</div><div class="text">Except where a party has changed its corporate name or merged with another corporation, this Agreement may not be assigned or otherwise transferred by either party in whole or part without the prior written consent of the other party to this Agreement.</div></div>
  </div>
  <div class="section-band" style="margin-top:12px;padding-left:41px">Amendments</div>
  <div class="body" style="padding-left:26px">
    <div class="clause"><div class="num">22.</div><div class="text">This Agreement may only be amended or modified by a written instrument executed by both the Company and the Evaluator.</div></div>
  </div>
  <div class="section-band" style="margin-top:10px;padding-left:41px">Governing Law</div>
  <div class="body" style="padding-left:26px">
    <div class="clause"><div class="num">23.</div><div class="text">This Agreement will be construed in accordance with and governed by the laws of the State of Michigan.</div></div>
  </div>
  <div class="section-band" style="margin-top:8px;padding-left:41px">General Provisions</div>
  <div class="body" style="padding-left:26px">
    <div class="clause" style="margin-bottom:5px"><div class="num">24.</div><div class="text">Time is of the essence in this Agreement.</div></div>
    <div class="clause" style="margin-bottom:5px"><div class="num">25.</div><div class="text">This Agreement may be executed in counterpart.</div></div>
    <div class="clause"><div class="num">26.</div><div class="text">Headings are inserted for the convenience of the parties only and are not to be considered when interpreting this Agreement. Words in the singular mean and include the plural and vice versa. Words in the masculine mean and include the feminine and vice versa.</div></div>
    <div class="clause"><div class="num">27.</div><div class="text">The clauses, paragraphs, and subparagraphs contained in this Agreement are intended to be read and construed independently of each other. If any part of this Agreement is held to be invalid, this invalidity will not affect the operation of any other part of this Agreement.</div></div>
    <div class="clause"><div class="num">28.</div><div class="text">The Evaluator is liable for all costs, expenses and expenditures including, and without limitation, the complete legal costs incurred by the Company in enforcing this Agreement as a result of any default of</div></div>
  </div>
  <footer class="page-footer"><div class="footer-brand"><span class="dot"></span>Terravista</div><div class="page-number">Page 7 of 8</div></footer>
</section>

<!-- Page 8 -->
<section class="page row-bottom col-4">
  <div class="body" style="padding-top:18px;padding-left:26px">
    <div class="clause" style="margin-bottom:6px"><div class="num"></div><div class="text">this Agreement by the Evaluator.</div></div>
    <div class="clause"><div class="num">29.</div><div class="text">The Company and the Evaluator acknowledge that this Agreement is reasonable, valid and enforceable. However, if a court of competent jurisdiction finds any of the provisions of this Agreement to be too broad to be enforceable, it is the intention of the Company and the Evaluator that such provision be reduced in scope by the court only to the extent deemed necessary by that court to render the provision reasonable and enforceable, bearing in mind that it is the intention of the Evaluator to give the Company the broadest possible protection against disclosure of the Confidential Information.</div></div>
    <div class="clause" style="margin-bottom:13px"><div class="num">30.</div><div class="text">No failure or delay by the Company in exercising any power, right or privilege provided in this Agreement will operate as a waiver, nor will any single or partial exercise of such rights, powers or privileges preclude any further exercise of them or the exercise of any other right, power or privilege provided in this Agreement.</div></div>
    <div class="clause"><div class="num">31.</div><div class="text">This Agreement will inure to the benefit of and be binding upon the respective heirs, executors, administrators, successors and assigns, as the case may be, of the Company and the Evaluator.</div></div>
    <div class="clause"><div class="num">32.</div><div class="text">This Agreement constitutes the entire agreement between the parties and there are no further items or provisions, either oral or otherwise.</div></div>
  </div>
  <div class="abs" style="left:26px;right:26px;top:229px">
    <b>IN WITNESS WHEREOF</b> ACME and COMPANY NAME have duly affixed their signatures under hand and seal on this <span class="rule" style="width:70px"></span>day of <span class="rule" style="width:31px"></span>, <span class="rule" style="width:22px"></span>.
  </div>
  <div class="signature" style="top:262px">ACME<br><br>Per:<span class="rule" style="width:85px"></span><br>(Seal)</div>
  <div class="signature" style="top:310px">COMPANY NAME<br><br>Per:<span class="rule" style="width:85px"></span><br>(Seal)</div>
  <footer class="page-footer"><div class="footer-brand"><span class="dot"></span>Terravista</div><div class="page-number">Page 8 of 8</div></footer>
</section>

</body>
</html>
```